Before & After School Care Business - Service Promotional Flyer

Need service promotional flyer for when parents (customers) are enrolling kids in school for first time. This flyer is specifically aimed at parents with kids aged 4 - 7 years old and needs to communicate crazy, fun and energy. We have five programs which we operate every school daily all based within local school halls. The flyer will be added to the local schools welcome to school pack. We also run School Holiday Programs supporting busy working families.

Industry/Entity Type

Business

```html
<!DOCTYPE html>
<html lang="en">
<head>
<meta charset="utf-8">
<title>Play Patch – Out of School Care Flyer</title>
<link rel="stylesheet" href="https://fonts.googleapis.com/css2?family=Baloo+2:wght@800&family=Amatic+SC:wght@700&family=Lato:ital,wght@0,400;1,700&display=swap">
<style>
  :root{
    --yellow:#ffe000;
    --yellow-light:#fff27a;
    --pink:#ec0b8d;
    --sky:#aedbe8;
    --green:#8cc63f;
    --blue:#14a3e0;
    --brown:#6e4a26;
    --card-yellow:#ffdf00;
    --red:#c4162f;
    --purple:#66278a;
    --teal:#15998f;
    --ink:#2b2b2b;
    --white:#ffffff;
    --page:#e9e6e1;
  }
  *{box-sizing:border-box;margin:0;padding:0}
  html,body{width:1200px;height:900px;overflow:hidden;background:var(--page)}
  .flyer{position:absolute;left:296px;top:20px;width:607px;height:860px;overflow:hidden;background:var(--white);font-family:'Lato',sans-serif;box-shadow:0 4px 14px rgba(0,0,0,.18)}
  .flyer__bg{position:absolute;inset:0}
  .photo{position:absolute;border:5px solid var(--white);box-shadow:0 2px 6px rgba(0,0,0,.3)}
  .photo--kids{border:none;box-shadow:none;left:12px;top:14px;width:290px;height:200px;border-radius:40% 40% 10% 10%;background:radial-gradient(circle at 50% 45%,#f0a35a,#d8452f 55%,#2f7fc8)}
  .photo--climb{left:24px;top:222px;width:170px;height:118px;transform:rotate(-9deg);background:linear-gradient(160deg,#7fb6e0,#c84b3a 60%,#3a3a3a)}
  .photo--ball{left:140px;top:282px;width:156px;height:124px;transform:rotate(5deg);background:linear-gradient(180deg,#8fc0e6,#b7c9b6 55%,#7a7a6e)}
  .photo--frame{left:24px;top:328px;width:166px;height:120px;transform:rotate(-3deg);background:linear-gradient(170deg,#9fcdf0,#3f9dc6 55%,#6b6b5e)}
  .headline{position:absolute;right:16px;top:34px;font-family:'Baloo 2',sans-serif;font-weight:800;line-height:.9;text-align:right;white-space:nowrap;transform:rotate(-4deg);text-shadow:2px 2px 0 var(--white),-2px -2px 0 var(--white),2px -2px 0 var(--white),-2px 2px 0 var(--white),3px 4px 6px rgba(0,0,0,.25)}
  .headline__line{display:block}
  .headline__line--1{font-size:40px}
  .headline__line--2{font-size:60px}
  .headline .green{color:var(--green)}
  .headline .pink{color:var(--pink)}
  .headline .blue{color:var(--blue)}
  .intro{position:absolute;left:314px;top:212px;width:276px;color:var(--white);font-size:11px;line-height:1.3;text-align:center}
  .intro__tag{font-weight:700;font-style:italic;display:block}
  .card{position:absolute;padding:14px 10px 12px;text-align:center;color:var(--white);box-shadow:0 3px 6px rgba(0,0,0,.3)}
  .card__title{font-family:'Amatic SC',sans-serif;font-weight:700;font-size:28px;line-height:.92;margin-bottom:9px}
  .card__text{font-size:10px;line-height:1.3}
  .card--spring{left:13px;top:440px;width:206px;height:160px;background:var(--brown);transform:rotate(-4deg)}
  .card--after{left:206px;top:413px;width:199px;height:148px;background:var(--card-yellow);color:var(--ink);padding-top:18px}
  .card--winter{left:398px;top:405px;width:196px;height:148px;background:var(--red);transform:rotate(3deg)}
  .card--before{left:87px;top:610px;width:205px;height:144px;background:var(--purple);padding-top:18px}
  .card--fullday{left:297px;top:588px;width:205px;height:148px;background:var(--teal);transform:rotate(5deg);padding-top:18px}
  .card--after .card__title{color:var(--ink)}
  .contact{position:absolute;left:52px;top:768px;font-size:12.5px;color:var(--ink);line-height:1.45;list-style:none}
  .contact li{display:flex;align-items:center;gap:7px}
  .contact svg{width:10px;height:10px;fill:#9a9a9a}
  .web{position:absolute;left:294px;top:768px;font-size:12.5px;color:var(--ink);display:flex;align-items:center;gap:7px}
  .web svg{width:10px;height:10px;stroke:#9a9a9a;fill:none}
  .social{position:absolute;left:306px;top:792px;display:flex;gap:9px}
  .social span{width:20px;height:20px;border-radius:50%;background:var(--blue)}
  .brand{position:absolute;left:482px;top:772px;display:flex;align-items:center;gap:7px}
  .brand__dot{width:14px;height:14px;border-radius:50%;background:var(--yellow)}
  .brand__name{font-family:'Baloo 2',sans-serif;font-weight:800;font-size:24px;color:var(--blue);line-height:.9}
</style>
</head>
<body>
<main class="flyer">
  <svg class="flyer__bg" width="607" height="860" viewBox="0 0 607 860" aria-hidden="true">
    <defs>
      <radialGradient id="sun" cx="0.45" cy="0.25" r="0.7">
        <stop offset="0" stop-color="var(--yellow-light)"/>
        <stop offset="1" stop-color="var(--yellow)"/>
      </radialGradient>
    </defs>
    <rect width="607" height="760" fill="url(#sun)"/>
    <path d="M0 380 C140 250 330 175 607 180 L607 760 L0 760 Z" fill="var(--white)"/>
    <path d="M0 392 C140 262 330 188 607 192 L607 760 L0 760 Z" fill="var(--pink)"/>
    <path d="M0 545 C180 540 330 545 430 560 C500 600 520 680 530 750 L0 750 Z" fill="var(--sky)"/>
    <rect y="749" width="607" height="92" fill="var(--white)"/>
    <rect y="841" width="607" height="19" fill="var(--sky)"/>
    <g class="confetti">
      <rect x="30" y="25" width="7" height="7" fill="var(--pink)" transform="rotate(20 33 28)"/>
      <rect x="65" y="60" width="6" height="9" fill="var(--teal)" transform="rotate(-30 68 64)"/>
      <rect x="392" y="20" width="7" height="7" fill="var(--blue)"/>
      <rect x="575" y="610" width="16" height="16" fill="var(--yellow)" transform="rotate(45 583 618)"/>
      <rect x="540" y="655" width="7" height="7" fill="var(--blue)" transform="rotate(30 543 658)"/>
      <circle cx="560" cy="681" r="14" fill="#e3271b"/>
    </g>
  </svg>

  <div class="photo photo--kids" role="img" aria-label="Group of cheerful children giving thumbs up"></div>
  <div class="photo photo--climb" role="img" aria-label="Children climbing playground equipment"></div>
  <div class="photo photo--ball" role="img" aria-label="Kids playing ball outdoors"></div>
  <div class="photo photo--frame" role="img" aria-label="Children on a climbing frame under blue sky"></div>

  <h1 class="headline">
    <span class="headline__line headline__line--1"><span class="green">Letting</span> <span class="pink">kids</span></span>
    <span class="headline__line headline__line--2"><span class="green">be</span> <span class="blue">kids</span></span>
  </h1>

  <p class="intro">For nearly 10 years we have been supporting kiwi families and local schools with yummy before school breakfast club’s, amazing after school care services &amp; awesome school holiday programmes. Find out for yourself why our families think we are welcoming, know how to have fun, are down to earth, hold onto old school values, are easy to use and actually care. And why our schools who we partner with value our programmes being in and part of their school.
    <span class="intro__tag">Play Patch - Let us be your kid’s awesome out of school care people</span>
  </p>

  <section class="card card--spring">
    <h2 class="card__title">School Holiday<br>Programme Spring</h2>
    <p class="card__text">Drop kids off for a yummy breakfast and we’ll send them to school smiling. After school they’ll enjoy a nutritious snack, games and activities; even help with homework if necessary.</p>
  </section>
  <section class="card card--after">
    <h2 class="card__title">After School Care</h2>
    <p class="card__text">Drop kids off for a yummy breakfast and we’ll send them to school smiling. After school they’ll enjoy a nutritious snack, games and activities; even help with homework if necessary.</p>
  </section>
  <section class="card card--winter">
    <h2 class="card__title">School Holiday<br>Programme Winter</h2>
    <p class="card__text">Drop kids off for a yummy breakfast and we’ll send them to school smiling. After school they’ll enjoy a nutritious snack, games and activities; even help with homework if necessary.</p>
  </section>
  <section class="card card--before">
    <h2 class="card__title">Before School Care</h2>
    <p class="card__text">Drop kids off for a yummy breakfast and we’ll send them to school smiling. After school they’ll enjoy a nutritious snack, games and activities; even help with homework if necessary.</p>
  </section>
  <section class="card card--fullday">
    <h2 class="card__title">Full Day Care</h2>
    <p class="card__text">Drop kids off for a yummy breakfast and we’ll send them to school smiling. After school they’ll enjoy a nutritious snack, games and activities; even help with homework if necessary.</p>
  </section>

  <ul class="contact">
    <li><svg viewBox="0 0 10 10"><path d="M5 0a3.5 3.5 0 0 0-3.5 3.5C1.5 6 5 10 5 10s3.5-4 3.5-6.5A3.5 3.5 0 0 0 5 0zm0 5a1.4 1.4 0 1 1 0-2.8A1.4 1.4 0 0 1 5 5z"/></svg>PO Box 48, Kapiti Bay, New Zealand</li>
    <li><svg viewBox="0 0 10 10"><path d="M0 2h10v6H0z M0 2l5 3.5L10 2" fill="none" stroke="#9a9a9a"/></svg>hello@playpatch.example</li>
    <li><svg viewBox="0 0 10 10"><path d="M2 0l2 2.5-1.2 1.2c.6 1.4 1.8 2.6 3.2 3.2L7.2 5.7 10 7.5 8.6 10C4 9.6.4 6 0 1.4z"/></svg>0800 555 0142</li>
  </ul>
  <div class="web"><svg viewBox="0 0 10 10"><circle cx="5" cy="5" r="4.3"/><path d="M.7 5h8.6M5 .7c-2.4 2.6-2.4 6 0 8.6M5 .7c2.4 2.6 2.4 6 0 8.6"/></svg>http://playpatch.example/</div>
  <div class="social" aria-label="Social links"><span></span><span></span><span></span><span></span></div>

  <div class="brand"><span class="brand__dot"></span><span class="brand__name">PLAY<br>PATCH</span></div>
</main>
</body>
</html>
```